GLACIVO SHAVED ICE FOOD TRUCK WEBSITE

SHAVED ICE MOBILE FOOD TRUCK WEBSITE WITH CONTENT AND MENU... SOCIALS ECT, WE ARE A MOBILE SHAVED ICE TRAILER THAT WILL BE WORKING PRIVATE EVENT'S, LOCAL EVENTS, SPORTING EVENTS AND CAN BE BOOKED OUT FOR PRIVATE PARTIES AND CORPERATE EVENTS

Target Market(s)

BIRTHDAYS, EVENTS,

Industry/Entity Type

SHAVED ICE FOOD TRUCK

Coding

Coded - Design and coding required

Number of Pages Required

4 page

Font styles to use
Serif

Colors
0054AA
0677BA
7BADD7
CADEEF
E8F1F8
0094D4
00A9DD
6FCCEA
C7EBF8
E9F6FB
EE7325
F08F49
F5BC92
FAE3D3
FDF4ED
EB3D1F
EC4F4E
F09395
F8D3D4
FCEDEE
E54698
E96AAD
F1A4CE
F9D9EA
FCEFF6

Requirements
Must have
• MY BRANDING THOUGH OUT THE WEBSITE AND FUN COOL THEME, NEED TO BE ABLE TO BOOK AN EVENT OR PARTY ONLINE AND LET PPL KNOW WHERE WE ARE AS WE ARE A MOBLIE UUNIT, NEEDS MENU
Nice to have
• A COOL FUN LOOK USING MY BRANDING AND LOGO WITH OUR CHARACTERS

```html
<!DOCTYPE html>
<html lang="en">
<head>
<meta charset="utf-8">
<title>Glacivo Shaved Ice</title>
<link href="https://fonts.googleapis.com/css2?family=Poppins:wght@400;500;600;700;800;900&display=swap" rel="stylesheet">
<style>
:root{
  --cyan:#14e1ec;
  --cyan-deep:#00c9d8;
  --pink:#f2679b;
  --pink-soft:#f9b6cf;
  --sky:#9fd6f2;
  --orange:#ff9d00;
  --orange-btn:#f5a300;
  --red:#ff0a50;
  --ink:#111;
  --muted:#6b6b6b;
  --paper:#fafafa;
  --violet:#7b5cf0;
  --green:#1fd69b;
  --rose:#ff3b8d;
}
*{margin:0;padding:0;box-sizing:border-box}
html,body{width:1200px;height:1200px;overflow:hidden;background:#fff;font-family:'Poppins',sans-serif;color:var(--ink)}
.stage{position:relative;width:1200px;height:1200px;overflow:hidden;background:#fff}
.panel{position:absolute;top:0;overflow:hidden;background:var(--paper)}
.panel--full{left:0;width:307px;height:1200px}
.panel--zoom{left:557px;width:643px;height:1200px;border-top:2px solid #333}
.page{position:absolute;left:0;top:0;width:1035px;height:4048px;transform-origin:0 0;background:var(--paper);overflow:hidden}
.panel--full .page{transform:scale(.2966)}
.panel--zoom .page{transform:scale(.6213)}
.abs{position:absolute}

/* hero */
.hero-bg{position:absolute;left:0;top:0;width:1035px;height:680px;
  clip-path:polygon(0 0,100% 0,100% 440px,0 675px);
  background:
   radial-gradient(ellipse 420px 160px at 700px 70px,rgba(255,255,255,.55),transparent 70%),
   radial-gradient(ellipse 500px 200px at 200px 620px,rgba(150,215,245,.95),transparent 75%),
   radial-gradient(ellipse 380px 200px at 980px 300px,rgba(160,215,245,.9),transparent 75%),
   linear-gradient(170deg,#fbc3d7 0%,#f57ba8 30%,#f2679b 55%,#f7a6c6 75%,#bfe4f6 100%);}
.nav{position:absolute;top:52px;left:48px;display:flex;gap:0;font-size:13px;font-weight:500}
.nav a{color:var(--ink);text-decoration:none;margin-right:35px}
.brand{position:absolute;left:460px;top:40px;width:120px;text-align:center}
.brand-dot{display:block;width:34px;height:34px;border-radius:50%;background:#1f4fb0;margin:0 auto 4px}
.brand-name{font-size:17px;font-weight:700;color:#1f4fb0;letter-spacing:1px}
.socials{position:absolute;top:55px;left:745px;display:flex;gap:13px}
.socials span{width:14px;height:14px;border-radius:3px;background:var(--ink)}
.btn-book{position:absolute;left:840px;top:42px;width:147px;height:43px;border-radius:22px;background:var(--cyan);font-size:10.5px;font-weight:500;display:flex;align-items:center;justify-content:center}
.tag{position:absolute;left:101px;top:150px;height:24px;padding:0 12px 0 26px;border-radius:12px;background:rgba(255,255,255,.18);font-size:11px;font-weight:500;line-height:24px}
.tag::before{content:"";position:absolute;left:9px;top:8px;width:9px;height:9px;border-radius:50%;background:rgba(255,255,255,.8)}
.hero-title{position:absolute;left:100px;top:196px;font-size:72px;line-height:83px;font-weight:800;color:var(--cyan);letter-spacing:-1px;text-shadow:0 2px 6px rgba(0,120,140,.35)}
.stars{position:absolute;left:101px;top:364px;display:flex;gap:13px}
.hero-copy{position:absolute;left:101px;top:390px;width:340px;font-size:13.3px;line-height:22.5px;font-weight:600}
.hero-art{position:absolute;left:560px;top:185px;width:410px;height:415px;border-radius:46% 54% 40% 60%/50% 45% 55% 50%;
  background:radial-gradient(circle at 65% 40%,#ffcc33,#ff7a1a 40%,#f0333a 65%,#2a8fe0 100%);opacity:.95}

/* about */
.about-title{position:absolute;left:133px;top:780px;font-size:34px;line-height:40px;font-weight:500}
.about-title u{text-decoration:none;box-shadow:inset 0 -5px 0 var(--cyan)}
.about-copy{position:absolute;left:524px;top:792px;width:385px;font-size:13.5px;line-height:22px;color:var(--muted)}
.feature{position:absolute;top:936px;width:220px;text-align:center;font-size:17px;font-weight:500}
.feature .ico{width:54px;height:54px;border-radius:50%;margin:0 auto 26px;display:flex;align-items:center;justify-content:center}

/* speciality */
.eyebrow{font-size:11px;font-weight:600;color:var(--cyan-deep);text-transform:uppercase}
.sec-head{font-size:34px;font-weight:500}
.sec-head u{text-decoration:none;box-shadow:inset 0 -4px 0 var(--pink)}
.spec-head{position:absolute;left:0;width:1035px;top:1302px;text-align:center}
.spec-head .sec-head{margin-top:10px}
.orbit{position:absolute;left:0;top:1400px}
.orbit-label{position:absolute;font-size:15px;font-weight:500;text-align:center;width:160px}
.orbit-art{position:absolute;left:332px;top:1655px;width:370px;height:400px;border-radius:46% 46% 30% 30%;
  background:radial-gradient(circle at 50% 30%,#ffd23a,#ff7a1a 35%,#ee2f3a 60%,#3ea7ea 85%,#eaf4fb 100%)}

/* testimonials */
.testi-head{position:absolute;left:624px;top:2305px}
.testi-head .sec-head{font-size:35px;line-height:40px;margin-top:6px}
.card{position:absolute;top:2497px;width:258px;height:275px;background:#fff;border-radius:4px;box-shadow:0 4px 18px rgba(0,0,0,.06);padding:28px 42px 0}
.card .av{width:28px;height:28px;border-radius:50%;background:#c9a38a;margin-bottom:6px}
.card h4{font-size:11px;font-weight:700}
.card small{display:block;font-size:9px;color:#999;margin-bottom:6px}
.card .rate{color:var(--orange);font-size:12px;letter-spacing:2px}
.card p{font-size:11px;line-height:21px;margin-top:6px}
.dots{position:absolute;left:605px;top:2802px;display:flex;gap:15px}
.dots span{width:6px;height:6px;border-radius:50%;background:#cde8f0}
.dots span.on{background:var(--cyan-deep)}
.blob-av{position:absolute;border-radius:50%;background:#7a5a48;border:3px solid #fff}

/* faq */
.faq-head{position:absolute;left:100px;top:3030px;width:400px}
.faq-head .sec-head{font-size:31px;line-height:40px;margin-top:8px}
.faq-item{position:absolute;left:505px;width:427px;height:59px;background:#fff;border:1px solid #eee;font-size:13px;font-weight:500;padding:0 40px 0 18px;line-height:59px}
.faq-item::after{content:"";position:absolute;right:18px;top:24px;width:8px;height:8px;border-right:2px solid var(--cyan-deep);border-bottom:2px solid var(--cyan-deep);transform:rotate(45deg)}
.faq-note{position:absolute;left:100px;top:3205px;width:300px;font-size:11px;line-height:21px;color:var(--muted)}
.faq-note b{display:block;color:var(--cyan-deep);font-size:10px;margin-bottom:8px}
.btn-contact{position:absolute;left:100px;top:3310px;width:128px;height:36px;border-radius:18px;background:var(--orange-btn);color:#fff;font-size:10px;display:flex;align-items:center;justify-content:center}

/* contact boxes */
.info{position:absolute;top:3373px;width:377px;height:147px;background:var(--red);color:#fff;padding:22px 0 0 98px}
.info h5{font-size:15px;font-weight:500;margin-bottom:12px}
.info p{font-size:10.5px;line-height:34px}
.info svg{position:absolute;left:0;top:40px}

/* newsletter */
.news-art{position:absolute;left:350px;top:3530px;width:330px;height:110px;border-radius:50% 50% 0 0;background:linear-gradient(180deg,rgba(255,160,60,.18),rgba(120,190,240,.15));}
.news-title{position:absolute;left:0;width:1035px;top:3620px;text-align:center;font-size:34px;line-height:40px;font-weight:500;color:var(--orange-btn)}
.news-input{position:absolute;left:310px;top:3705px;width:300px;height:42px;font-size:11px;line-height:42px;padding-left:20px;color:#555}
.news-btn{position:absolute;left:612px;top:3705px;width:111px;height:42px;border-radius:0 21px 21px 0;background:var(--orange-btn);color:#fff;font-size:11px;display:flex;align-items:center;justify-content:center}

/* footer */
.footer{position:absolute;left:0;top:3720px;width:1035px;height:330px}
.foot-brand{position:absolute;left:150px;top:3840px;text-align:center}
.foot-brand .brand-dot{width:60px;height:60px;background:#fff}
.foot-brand .brand-name{color:#fff;font-size:24px}
.foot-col{position:absolute;top:3878px;color:#fff;text-align:center;font-size:12px;font-weight:500}
.foot-col .row{display:flex;gap:14px;justify-content:center;margin-top:20px}
.foot-col .row span{width:18px;height:18px;border-radius:50%;background:#fff}
.foot-col .mail{color:var(--cyan);margin-top:12px}
.copy{position:absolute;left:0;width:1035px;top:4026px;text-align:center;font-size:9px;color:#fff}
</style>
</head>
<body>
<div class="stage">

<!-- full page overview -->
<div class="panel panel--full">
<div class="page">
  <div class="hero-bg"></div>
  <nav class="nav"><a>Home</a><a>About Us</a><a>Menu</a><a>Feedback</a><a>Contact Us</a></nav>
  <div class="brand"><span class="brand-dot"></span><span class="brand-name">GLACIVO</span></div>
  <div class="socials"><span></span><span></span><span></span></div>
  <div class="btn-book">Book an Event</div>
  <div class="tag">GLACIVO.FUN</div>
  <h1 class="hero-title">COME CHILL<br>WITH US</h1>
  <div class="stars">
    <svg width="184" height="26" viewBox="0 0 184 26"><g fill="#ff9d00"><path id="st" d="M13 0l3.8 8.3 9.2 1-6.8 6.2 1.9 9L13 20 4.9 24.5l1.9-9L0 9.3l9.2-1z"/><use href="#st" x="40"/><use href="#st" x="79"/><use href="#st" x="118"/><use href="#st" x="158"/></g></svg>
  </div>
  <p class="hero-copy">Served exceptional desserts to the surrounding community for over a decade offering both in-store and catering services.</p>
  <div class="hero-art" role="img" aria-label="Mascot character in sunglasses beside a cup of rainbow shaved ice"></div>

  <h2 class="about-title">Authentic<br><u>Shaved Ice</u></h2>
  <p class="about-copy">Creating a treat that’s as refreshing as it is unforgettable. With every bite, you’ll taste the love and care that makes our shave ice truly special.</p>
  <div class="feature" style="left:145px"><div class="ico" style="background:#fde6dc"><svg width="22" height="22" viewBox="0 0 24 24" fill="none" stroke="#f26a3a" stroke-width="2"><path d="M7 10v11H3V10zM7 10l4-8c2 0 3 1 3 3v3h6a2 2 0 0 1 2 2l-2 9a2 2 0 0 1-2 2H7"/></svg></div>Fresh To Order</div>
  <div class="feature" style="left:407px"><div class="ico" style="background:#d6f6f6"><svg width="22" height="22" viewBox="0 0 24 24" fill="#1ccfcf"><path d="M1 5h13v11H1zM14 9h5l4 4v3h-9z"/><circle cx="5" cy="18" r="2.5"/><circle cx="18" cy="18" r="2.5"/></svg></div>Delivery or Pick-Up</div>
  <div class="feature" style="left:668px"><div class="ico" style="background:#fbe3f6"><svg width="20" height="20" viewBox="0 0 24 24" fill="#f03fc8"><circle cx="8.5" cy="14" r="7"/><circle cx="15.5" cy="14" r="7"/><rect x="11" y="2" width="2" height="6"/></svg></div>Quality Ingredients</div>

  <div class="spec-head"><div class="eyebrow">Original Flavors</div><h2 class="sec-head">Our <u>Speciality</u></h2></div>
  <svg class="orbit" width="1035" height="860" viewBox="0 0 1035 860">
    <circle cx="517" cy="455" r="385" fill="none" stroke="#ddd" stroke-dasharray="2 6"/>
    <circle cx="517" cy="455" r="295" fill="none" stroke="#ddd" stroke-dasharray="2 6"/>
    <circle cx="517" cy="455" r="205" fill="#f0f1f4"/>
    <circle cx="540" cy="158" r="22" fill="#ffb400"/><path d="M540 148l3 7 7 .5-5.5 4.5 2 7-6.5-4-6.5 4 2-7-5.5-4.5 7-.5z" fill="none" stroke="#fff" stroke-width="1.5"/>
    <circle cx="285" cy="336" r="22" fill="var(--green)"/><path d="M276 345c0-10 8-18 18-18 0 10-8 18-18 18z" fill="none" stroke="#fff" stroke-width="1.8"/>
    <circle cx="750" cy="336" r="22" fill="var(--violet)"/><path d="M740 338a10 8 0 0 1 20 0zM750 338v9" fill="none" stroke="#fff" stroke-width="1.8"/>
    <circle cx="300" cy="540" r="22" fill="var(--rose)"/><circle cx="300" cy="541" r="6" fill="none" stroke="#fff" stroke-width="1.8"/>
    <circle cx="735" cy="540" r="22" fill="#22c7d6"/><circle cx="735" cy="540" r="6" fill="none" stroke="#fff" stroke-width="1.8"/>
    <rect x="298" y="199" width="8" height="8" fill="none" stroke="#f5a0a0" transform="rotate(45 302 203)"/>
    <path d="M676 150l8 8M684 150l-8 8" stroke="#f07" stroke-width="1.2"/>
    <circle cx="212" cy="421" r="3.5" fill="none" stroke="#7fd7e2"/>
    <circle cx="802" cy="421" r="3.5" fill="none" stroke="#f5d050"/>
    <circle cx="733" cy="636" r="3.5" fill="none" stroke="#7fd7e2"/>
  </svg>
  <div class="orbit-label" style="left:458px;top:1456px">Trusted &amp; strong<br>security</div>
  <div class="orbit-label" style="left:121px;top:1637px">Favorites</div>
  <div class="orbit-label" style="left:754px;top:1637px">Add-Ons</div>
  <div class="orbit-label" style="left:145px;top:1882px">Flavors</div>
  <div class="orbit-label" style="left:754px;top:1882px">Savory</div>
  <div class="orbit-art" role="img" aria-label="Cup of rainbow shaved ice"></div>

  <svg class="abs" style="left:0;top:2300px" width="540" height="640" viewBox="0 0 540 640" role="img" aria-label="Colourful abstract blob behind testimonials">
    <defs><linearGradient id="bl" x1="0" y1="0" x2="1" y2="1"><stop offset="0" stop-color="#ffb000"/><stop offset=".35" stop-color="#e94fd0"/><stop offset=".6" stop-color="#a86bf0"/><stop offset="1" stop-color="#34c3f0"/></linearGradient></defs>
    <path d="M0 90C140 20 330 -10 470 60c90 50 70 180 10 300-60 140-130 250-240 270C120 650 20 600 0 560z" fill="url(#bl)"/>
  </svg>
  <div class="blob-av" style="left:280px;top:2305px;width:52px;height:52px"></div>
  <div class="blob-av" style="left:5px;top:2435px;width:44px;height:44px"></div>
  <div class="blob-av" style="left:265px;top:2847px;width:52px;height:52px"></div>
  <div class="blob-av" style="left:25px;top:2805px;width:34px;height:34px;background:#2a5bd0"></div>
  <div class="testi-head"><div class="eyebrow" style="text-transform:none">Testimonials</div><h2 class="sec-head">You’re gonna love<br>us <u>forever.</u></h2></div>
  <div class="card" style="left:100px"><div class="av"></div><h4>Rosa Lind</h4><small>England</small><div class="rate">★★★★★</div><p>"Nimbus is worth much more than I paid. We've seen amazing results already. I will recommend you."</p></div>
  <div class="card" style="left:383px"><div class="av" style="background:#5b4638"></div><h4>Theo Marsh</h4><small>Canada</small><div class="rate">★★★★★</div><p>"Nimbus is worth much more than I paid. Dude, your stuff is the bomb! We've seen amazing results already."</p></div>
  <div class="card" style="left:666px"><div class="av" style="background:#b48a6a"></div><h4>Ivy Carden</h4><small>France</small><div class="rate">★★★★★</div><p>"Nimbus was the best investment I ever made. I would be lost without Nimbus. Thanks for the great service."</p></div>
  <div class="card" style="left:949px"><div class="av"></div><h4>Theo Marsh</h4><small>USA</small><div class="rate">★★★★★</div><p>"It's really great, Nimbus, we'd be bankrupt without it. I recommend it."</p></div>
  <div class="dots"><span></span><span></span><span class="on"></span><span></span><span></span></div>

  <div class="faq-head"><div class="eyebrow" style="text-transform:none">Questions &amp; Answers</div><h2 class="sec-head">Have any<br>questions? <u>Find</u> answers<br>here.</h2></div>
  <div class="faq-item" style="top:3030px">How does the free trial work?</div>
  <div class="faq-item" style="top:3105px">How do you weigh different criteria in process?</div>
  <div class="faq-item" style="top:3180px">What does Nimbus look for in an idea?</div>
  <div class="faq-item" style="top:3254px">What do you look for in a founding team?</div>
  <p class="faq-note"><b>Confusion?</b>Didn't find your answer here? Just send us a message and we'll help in no time.</p>
  <div class="btn-contact">Contact us</div>

  <div class="info" style="left:132px">
    <svg width="60" height="60" viewBox="0 0 60 60" fill="none" stroke="#5ee6f0" stroke-width="2.5"><path d="M4 18l14-6 16 6 16-6v36l-16 6-16-6-14 6z"/><path d="M38 8a8 8 0 0 1 16 0c0 7-8 14-8 14s-8-7-8-14z"/></svg>
    <h5>Our Address</h5><p>2280 - HARBOR LN #12<br>SEAVIEW CA, 90000</p></div>
  <div class="info" style="left:524px">
    <svg width="60" height="60" viewBox="0 0 60 60" fill="none" stroke="#5ee6f0" stroke-width="2.5"><rect x="14" y="4" width="30" height="52" rx="3"/><path d="M14 14h30M14 44h30"/></svg>
    <h5>Contact Info</h5><p>+1 555-014-2290</p></div>

  <div class="news-art" role="img" aria-label="Faded mascot characters peeking over the signup"></div>
  <h2 class="news-title">Sign up and receive our promotions<br>and events in your email.</h2>
  <div class="news-input">you@mailbox.com</div>
  <div class="news-btn">Register</div>

  <svg class="footer" width="1035" height="330" viewBox="0 0 1035 330" preserveAspectRatio="none">
    <path d="M0 20c120-30 220 30 360 5s260-35 380 0 200 10 295-15v330H0z" fill="#22dbe6"/>
    <path d="M0 45c150-25 300 20 460 0s320-30 575 5v285H0z" fill="#fff"/>
    <path d="M0 55c150-20 300 15 460 0s320-25 575 5v270H0z" fill="#ff9a00"/>
    <path d="M0 105c170-25 330 15 520-5s330-15 515 5v225H0z" fill="var(--red)"/>
  </svg>
  <div class="foot-brand"><span class="brand-dot"></span><span class="brand-name">GLACIVO</span></div>
  <div class="foot-col" style="left:417px;width:200px">Find us on social media<div class="row"><span></span><span></span><span></span></div></div>
  <div class="foot-col" style="left:700px;width:220px">We're always happy to help.<div class="mail">hello@glacivo.fun</div></div>
  <div class="copy">© 2025 GLACIVO. All rights reserved.</div>
</div>
</div>

<!-- zoomed top of page -->
<div class="panel panel--zoom">
<div class="page">
  <div class="hero-bg"></div>
  <nav class="nav"><a>Home</a><a>About Us</a><a>Menu</a><a>Feedback</a><a>Contact Us</a></nav>
  <div class="brand"><span class="brand-dot"></span><span class="brand-name">GLACIVO</span></div>
  <div class="socials"><span></span><span></span><span></span></div>
  <div class="btn-book">Book an Event</div>
  <div class="tag">GLACIVO.FUN</div>
  <h1 class="hero-title">COME CHILL<br>WITH US</h1>
  <div class="stars">
    <svg width="184" height="26" viewBox="0 0 184 26"><g fill="#ff9d00"><path id="st2" d="M13 0l3.8 8.3 9.2 1-6.8 6.2 1.9 9L13 20 4.9 24.5l1.9-9L0 9.3l9.2-1z"/><use href="#st2" x="40"/><use href="#st2" x="79"/><use href="#st2" x="118"/><use href="#st2" x="158"/></g></svg>
  </div>
  <p class="hero-copy">Served exceptional desserts to the surrounding community for over a decade offering both in-store and catering services.</p>
  <div class="hero-art" role="img" aria-label="Mascot character in sunglasses beside a cup of rainbow shaved ice"></div>

  <h2 class="about-title">Authentic<br><u>Shaved Ice</u></h2>
  <p class="about-copy">Creating a treat that’s as refreshing as it is unforgettable. With every bite, you’ll taste the love and care that makes our shave ice truly special.</p>
  <div class="feature" style="left:145px"><div class="ico" style="background:#fde6dc"><svg width="22" height="22" viewBox="0 0 24 24" fill="none" stroke="#f26a3a" stroke-width="2"><path d="M7 10v11H3V10zM7 10l4-8c2 0 3 1 3 3v3h6a2 2 0 0 1 2 2l-2 9a2 2 0 0 1-2 2H7"/></svg></div>Fresh To Order</div>
  <div class="feature" style="left:407px"><div class="ico" style="background:#d6f6f6"><svg width="22" height="22" viewBox="0 0 24 24" fill="#1ccfcf"><path d="M1 5h13v11H1zM14 9h5l4 4v3h-9z"/><circle cx="5" cy="18" r="2.5"/><circle cx="18" cy="18" r="2.5"/></svg></div>Delivery or Pick-Up</div>
  <div class="feature" style="left:668px"><div class="ico" style="background:#fbe3f6"><svg width="20" height="20" viewBox="0 0 24 24" fill="#f03fc8"><circle cx="8.5" cy="14" r="7"/><circle cx="15.5" cy="14" r="7"/><rect x="11" y="2" width="2" height="6"/></svg></div>Quality Ingredients</div>

  <div class="spec-head"><div class="eyebrow">Original Flavors</div><h2 class="sec-head">Our <u>Speciality</u></h2></div>
  <svg class="orbit" width="1035" height="860" viewBox="0 0 1035 860">
    <circle cx="517" cy="455" r="385" fill="none" stroke="#ddd" stroke-dasharray="2 6"/>
    <circle cx="517" cy="455" r="295" fill="none" stroke="#ddd" stroke-dasharray="2 6"/>
    <circle cx="517" cy="455" r="205" fill="#f0f1f4"/>
    <circle cx="540" cy="158" r="22" fill="#ffb400"/><path d="M540 148l3 7 7 .5-5.5 4.5 2 7-6.5-4-6.5 4 2-7-5.5-4.5 7-.5z" fill="none" stroke="#fff" stroke-width="1.5"/>
    <circle cx="285" cy="336" r="22" fill="var(--green)"/><path d="M276 345c0-10 8-18 18-18 0 10-8 18-18 18z" fill="none" stroke="#fff" stroke-width="1.8"/>
    <circle cx="750" cy="336" r="22" fill="var(--violet)"/><path d="M740 338a10 8 0 0 1 20 0zM750 338v9" fill="none" stroke="#fff" stroke-width="1.8"/>
    <circle cx="300" cy="540" r="22" fill="var(--rose)"/>
    <circle cx="735" cy="540" r="22" fill="#22c7d6"/>
    <rect x="298" y="199" width="8" height="8" fill="none" stroke="#f5a0a0" transform="rotate(45 302 203)"/>
    <path d="M676 150l8 8M684 150l-8 8" stroke="#f07" stroke-width="1.2"/>
    <circle cx="212" cy="421" r="3.5" fill="none" stroke="#7fd7e2"/>
    <circle cx="802" cy="421" r="3.5" fill="none" stroke="#f5d050"/>
  </svg>
  <div class="orbit-label" style="left:458px;top:1456px">Trusted &amp; strong<br>security</div>
  <div class="orbit-label" style="left:121px;top:1637px">Favorites</div>
  <div class="orbit-label" style="left:754px;top:1637px">Add-Ons</div>
  <div class="orbit-label" style="left:145px;top:1882px">Flavors</div>
  <div class="orbit-label" style="left:754px;top:1882px">Savory</div>
  <div class="orbit-art" role="img" aria-label="Cup of rainbow shaved ice"></div>
</div>
</div>

</div>
</body>
</html>
```